Young Accounting firm needing a captivating business card

We need a business card design that forces the person to look at the card because its either gold foil, plastic, or lettering pop up etc. We already have a logo with a specific gold color and we need to make it pop. We are an accounting firm. I need the words" accounting, payroll, licenses, audits, taxes" somewhere on the business card so as to describe what we do- preferably on the side where the logo is at.

Industry/Entity Type

Accounting

Contact Information for Business Card

Address 48276 9th Ave S Ste 305, Federal Way, WA 98117
Business Phone (360)418-2096
Fax (360)418-2157
Office Cell Phone (360)586-7319

Font styles to use
Serif

Colors
85abd2

Requirements
Must have
• It should state
• "Accounting" "Taxes" "Audits" "Licenses" "Payroll"
Nice to have
• Matte with gold foil, different textures, With Either a textured ivory background or gray blue slate background
Should not have
• colorful colors

```html
<!DOCTYPE html>
<html lang="en">
<head>
<meta charset="UTF-8">
<title>KRLedgerline Business Card</title>
<link rel="stylesheet" href="https://fonts.googleapis.com/css2?family=Lora:wght@400;500&display=swap">
<style>
  :root {
    --backdrop: #e9e6e0;
    --card-side: #f5e6bf;
    --card-base: #fcf5df;
    --card-top: #ffffff;
    --gold: #b89a2e;
    --gold-text: #b08a22;
    --brown: #7a5a1e;
    --band-text: #4a3410;
  }
  html, body {
    margin: 0;
    padding: 0;
    width: 1200px;
    height: 834px;
    overflow: hidden;
    background: var(--backdrop);
  }
  .canvas {
    position: relative;
    width: 1200px;
    height: 834px;
  }
  .card {
    position: absolute;
    left: 100px;
    top: 134px;
    width: 1000px;
    height: 567px;
    background: var(--card-base);
    box-shadow: 0 6px 18px rgba(0,0,0,0.18);
    overflow: hidden;
  }
  .card-shapes {
    position: absolute;
    inset: 0;
  }
  .brand {
    position: absolute;
    top: 150px;
    left: 0;
    width: 1000px;
    height: 60px;
    display: flex;
    justify-content: center;
    align-items: center;
    gap: 16px;
  }
  .brand-square {
    width: 32px;
    height: 32px;
    background: var(--gold-text);
  }
  .brand-name {
    font-family: "Lora", serif;
    font-weight: 500;
    font-size: 46px;
    line-height: 60px;
    color: var(--gold-text);
  }
  .contact {
    position: absolute;
    top: 305px;
    left: 0;
    width: 1000px;
    text-align: center;
    font-family: "Lora", serif;
    font-size: 27px;
    line-height: 34px;
    color: var(--brown);
  }
  .contact p { margin: 0; }
  .services {
    position: absolute;
    top: 489px;
    left: 0;
    width: 1000px;
    height: 78px;
    display: flex;
    align-items: center;
    justify-content: center;
    font-family: "Lora", serif;
    font-weight: 500;
    font-size: 30px;
    color: var(--band-text);
  }
</style>
</head>
<body>
<div class="canvas">
  <div class="card">
    <svg class="card-shapes" width="1000" height="567" viewBox="0 0 1000 567">
      <polygon class="side-panel-left" points="0,0 254,237 0,567" fill="var(--card-side)"/>
      <polygon class="side-panel-right" points="1000,0 753,237 1000,567" fill="var(--card-side)"/>
      <polygon class="top-panel" points="0,0 1000,0 753,237 254,237" fill="var(--card-top)"/>
      <polygon class="service-band" points="93,489 917,489 948,567 62,567" fill="var(--gold)"/>
    </svg>
    <div class="brand">
      <div class="brand-square"></div>
      <div class="brand-name">KRLedgerline</div>
    </div>
    <div class="contact">
      <p>Address 48276 9th Ave S Ste 305, Federal Way, WA 98117</p>
      <p>Business Phone (360)418-2096</p>
      <p>Fax (360)418-2157</p>
      <p>Office Cell Phone (360)586-7319</p>
    </div>
    <div class="services">accounting / payroll / licenses / audits / taxes</div>
  </div>
</div>
</body>
</html>
```